Corporate Template

Looking for a set of corporate slides to be made which contain multiple different slides and orientations. Looking for at least 8 to 10 different master pages plus a Coversheet and closeout page. Incorporating a color palate similar to our logo coloring is preferred.

I have attached a logo.

```html
<!DOCTYPE html>
<html lang="en">
<head>
<meta charset="utf-8">
<title>Getting Start Process</title>
<link rel="stylesheet" href="https://fonts.googleapis.com/css2?family=Great+Vibes&family=Arimo:wght@400;700&family=Gelasio:wght@400;700&display=swap">
<style>
  :root {
    --blue-deep: #0a4a98;
    --blue-mid: #1170c8;
    --blue-light: #1e90e6;
    --teal: #14c9b6;
    --orange: #f7941d;
    --lime: #e6ff2b;
    --slate: #555658;
    --track-dark: #2b2d30;
    --track-mid: #4a4d52;
    --white: #ffffff;
    --footer-text: #7a7c80;
    --brand-blue: #1a5fa8;
  }
  html, body {
    margin: 0;
    padding: 0;
    width: 1200px;
    height: 900px;
    overflow: hidden;
    background: var(--white);
  }
  .slide {
    position: relative;
    width: 1200px;
    height: 900px;
    overflow: hidden;
    background: linear-gradient(180deg, var(--blue-deep) 0%, var(--blue-mid) 45%, var(--blue-light) 100%);
    font-family: "Gelasio", Georgia, serif;
    color: var(--white);
  }
  .side-rail {
    position: absolute;
    top: 0;
    right: 0;
    width: 35px;
    height: 900px;
    background: var(--slate);
  }
  .corner-shape {
    position: absolute;
    top: 0;
    left: 0;
  }
  .title {
    position: absolute;
    inset: 0 auto auto 0;
    margin: 0;
    font-weight: 400;
  }
  .title-script {
    position: absolute;
    left: 618px;
    top: 48px;
    white-space: nowrap;
    font-family: "Great Vibes", cursive;
    font-size: 56px;
    line-height: 1;
    letter-spacing: 5px;
    color: rgba(255,255,255,0.88);
  }
  .title-caps {
    position: absolute;
    left: 940px;
    top: 60px;
    white-space: nowrap;
    font-family: "Arimo", Arial, sans-serif;
    font-weight: 700;
    font-size: 38px;
    line-height: 1;
    color: var(--white);
  }
  .shapes {
    position: absolute;
    inset: 0;
  }
  .copy {
    position: absolute;
    margin: 0;
    font-size: 27px;
    line-height: 36px;
  }
  .copy-call { left: 72px; top: 254px; width: 300px; }
  .copy-questions { left: 72px; top: 544px; width: 300px; }
  .copy-current { left: 464px; top: 251px; width: 690px; }
  .copy-ready { left: 464px; top: 541px; width: 690px; }
  .footer {
    position: absolute;
    left: 0;
    bottom: 0;
    width: 1165px;
    height: 72px;
    background: var(--white);
  }
  .pager {
    position: absolute;
    left: 37px;
    top: 24px;
    font-family: "Arimo", Arial, sans-serif;
    font-weight: 700;
    font-size: 15px;
    color: var(--footer-text);
    word-spacing: 1px;
  }
  .pager .current {
    color: var(--brand-blue);
    font-size: 21px;
  }
  .brand {
    position: absolute;
    right: 382px;
    top: 25px;
    display: flex;
    align-items: center;
    gap: 8px;
    font-family: "Gelasio", Georgia, serif;
    font-weight: 400;
    font-size: 15px;
    color: var(--brand-blue);
  }
  .brand-mark {
    width: 16px;
    height: 16px;
    background: var(--brand-blue);
  }
  .footer-divider {
    position: absolute;
    left: 800px;
    top: 7px;
    width: 2px;
    height: 58px;
    background: var(--slate);
  }
  .site {
    position: absolute;
    left: 818px;
    top: 25px;
    font-family: "Gelasio", Georgia, serif;
    font-weight: 700;
    font-size: 16px;
    color: var(--slate);
  }
</style>
</head>
<body>
<main class="slide">
  <svg class="corner-shape" width="1200" height="200" viewBox="0 0 1200 200">
    <polygon points="750,0 1070,0 930,152" fill="var(--teal)"/>
  </svg>

  <h1 class="title"><span class="title-script">Getting Start</span><span class="title-caps">PROCESS</span></h1>

  <svg class="shapes" width="1200" height="900" viewBox="0 0 1200 900">
    <defs>
      <linearGradient id="trackTone" x1="0" y1="0" x2="1" y2="1">
        <stop offset="0" stop-color="var(--track-mid)"/>
        <stop offset="1" stop-color="var(--track-dark)"/>
      </linearGradient>
    </defs>
    <g role="img" aria-label="Photo of running track lane numbers">
      <polygon points="72,148 368,148 396,231 72,231" fill="url(#trackTone)"/>
    </g>
    <polygon class="band-orange" points="72,230 388,230 398,251 72,251" fill="var(--orange)"/>
    <polygon class="band-orange" points="72,512 388,512 398,539 72,539" fill="var(--orange)"/>
    <polygon class="band-lime" points="466,230 1088,230 1098,251 466,251" fill="var(--lime)"/>
    <g role="img" aria-label="Photo of running track lane numbers">
      <polygon points="466,434 1050,434 1078,516 466,516" fill="url(#trackTone)"/>
    </g>
    <polygon class="band-lime" points="466,515 1088,515 1100,539 466,539" fill="var(--lime)"/>
  </svg>

  <p class="copy copy-call">Let’s get started!<br>The easiest way to get the ball rolling is to give us a quick phone call or send us an email.</p>
  <p class="copy copy-questions">One of our sales associates will ask you a few questions so we can take the next steps in getting your product manufactured.</p>
  <p class="copy copy-current">Is your product currently being manufactured?<br>If so, why are you interested in finding another rotational molder?</p>
  <p class="copy copy-ready">Do you have engineered drawings?<br>Do you have fabricated molds for your product(s)?<br>What is your timeline?</p>

  <div class="side-rail"></div>

  <footer class="footer">
    <div class="pager">1 | 2 &nbsp;| 3 | 4 | 5 | <span class="current">6</span> | 7 | 8 | 9</div>
    <div class="brand"><span class="brand-mark"></span>Larkspur Molding</div>
    <div class="footer-divider"></div>
    <div class="site">www.larkspurmolding.com</div>
  </footer>
</main>
</body>
</html>
```